Flyer Design Project

Advertising - The header is the most important thing on this flyer, I would like to see an eyes-popping more in dept look of the clouds along with the sport car of the couple on the road. The symbol of the "Lantern Over Amber Hills" don't want it there. Just replace it with a regular "i".

Industry/Entity Type

Advertising

Requirements
Must have
• head turning... stopping prospects to read the flyer... everything got to be on point from art works to different fonts and style.

```html
<!DOCTYPE html>
<html lang="en">
<head>
<meta charset="utf-8">
<title>Lantern Over Amber Hills – Flyer</title>
<link href="https://fonts.googleapis.com/css2?family=Montserrat:wght@300;700;800&family=Oswald:wght@500;600;700&family=Lato:wght@400;700;900&family=Orbitron:wght@700&display=swap" rel="stylesheet">
<style>
  :root{
    --red:#c0181d;
    --red-dark:#8e0e12;
    --maroon:#4e0507;
    --blue:#2aa3ea;
    --blue-band:#2e9fe6;
    --navy:#152b52;
    --black:#0e0e0f;
    --ink:#1d1d1f;
    --white:#ffffff;
    --grey:#444;
  }
  *{box-sizing:border-box;margin:0;padding:0}
  html,body{width:907px;height:1200px;overflow:hidden;background:var(--white)}
  .flyer{position:relative;width:907px;height:1200px;overflow:hidden;background:var(--white);font-family:"Lato",sans-serif;color:var(--ink)}

  /* Header */
  .hero-photo{position:absolute;left:0;top:0;width:907px;height:358px;
    background:
      linear-gradient(90deg,rgba(255,255,255,0) 0%,rgba(255,255,255,0) 50%,rgba(255,255,255,.85) 66%,#fff 76%),
      linear-gradient(180deg,#7d8ea3 0%,#c9c2b0 22%,#f3e6c7 40%,#e7d3ad 52%,#b8321e 62%,#c5291c 78%,#6e2a1d 100%);}
  .title{position:absolute;right:30px;top:44px;text-align:right;line-height:1}
  .title .line-1{display:block;font-family:"Montserrat",sans-serif;font-weight:300;font-size:46px;color:var(--ink);letter-spacing:.5px}
  .title .line-2{display:block;font-family:"Montserrat",sans-serif;font-weight:800;font-size:58px;color:var(--blue);margin-top:4px}
  .title .line-3{display:block;font-family:"Montserrat",sans-serif;font-weight:800;font-size:46px;color:var(--red);margin-top:4px}
  .stripe{position:absolute;left:0;top:355px;width:907px;height:12px;background:var(--blue-band)}

  /* Right column */
  .info-panel{position:absolute;left:544px;top:367px;width:363px;height:723px;
    background:linear-gradient(180deg,#1b1b1d 0%,var(--black) 100%)}
  .badge{position:absolute;left:570px;top:232px;width:300px;height:300px;border-radius:50%;
    background:radial-gradient(circle at 45% 35%,#d6262b 0%,var(--red) 50%,var(--red-dark) 100%);
    border:8px solid var(--white);display:flex;flex-direction:column;align-items:center;justify-content:center;
    text-align:center;color:var(--white);font-family:"Lato",sans-serif;font-weight:900;line-height:1.12}
  .badge .big{font-size:33px}
  .badge .mid{font-size:22px}
  .badge .dark{color:var(--maroon)}
  .badge .small{font-size:19px}
  .badge .cta{font-size:22px;color:var(--maroon);margin-top:2px}

  .hours{position:absolute;left:565px;top:540px;color:var(--white)}
  .label-blue{font-family:"Oswald",sans-serif;font-weight:500;color:var(--blue);font-size:25px;line-height:1.2}
  .day{font-family:"Lato",sans-serif;font-weight:900;font-size:19px;line-height:1.3}
  .time{font-family:"Lato",sans-serif;font-weight:900;font-size:18px;color:var(--blue);line-height:1.35;margin-bottom:6px}
  .phone{position:absolute;left:565px;color:var(--red);font-family:"Oswald",sans-serif;font-weight:600;font-size:31px;line-height:1}
  .phone-main{top:694px}
  .note{position:absolute;left:565px;color:var(--white);font-weight:900;font-size:15.5px;line-height:1.3}
  .note-pin{top:744px}
  .pin{position:absolute;left:565px;top:794px;color:var(--red);font-family:"Oswald",sans-serif;font-weight:500;font-size:28px;line-height:1.3}
  .info-line{position:absolute;left:565px;top:890px;font-family:"Lato",sans-serif;font-weight:900;font-size:19px;color:var(--blue)}
  .phone-info{top:932px}
  .note-listen{top:975px}
  .web-label{position:absolute;left:565px;top:1024px;font-weight:900;font-size:19px;color:var(--blue)}
  .web-url{position:absolute;left:565px;top:1054px;font-size:18px;color:var(--white);font-weight:400}

  /* Left column */
  .intro{position:absolute;left:26px;top:402px;width:510px}
  .intro h2{font-family:"Oswald",sans-serif;font-weight:600;font-size:28px;line-height:1.18;color:var(--red);letter-spacing:.3px}
  .intro h2 .dark{display:block;color:var(--ink)}
  .intro p{font-size:14.4px;line-height:1.38;color:var(--grey);margin-top:10px}
  .intro p + p{margin-top:8px}
  .intro strong{color:var(--ink)}

  .section-bar{position:absolute;left:0;width:544px;background:var(--blue-band);color:var(--white);
    font-family:"Orbitron",sans-serif;font-weight:700;padding-left:38px;display:flex;align-items:center;white-space:nowrap;overflow:hidden}
  .bar-how{top:601px;height:33px;font-size:20px}
  .bar-speak{top:752px;height:68px;font-size:23px;line-height:1.3;padding-left:24px}

  .steps{position:absolute;left:26px;top:650px;width:510px;list-style:none}
  .steps li{display:flex;font-size:14.4px;line-height:1.3;color:var(--ink);margin-bottom:3px}
  .steps .num{width:36px;font-family:"Oswald",sans-serif;font-weight:600;color:var(--red);font-size:14px}
  .steps .rule{width:116px;border-bottom:1px solid var(--ink);height:14px;margin-right:6px;flex:none}

  .benefits{position:absolute;left:26px;top:846px;width:505px;list-style:none}
  .benefits li{position:relative;padding-left:22px;font-size:14.3px;line-height:1.3;color:var(--ink);margin-bottom:4px}
  .benefits svg{position:absolute;left:0;top:2px}
  .benefits strong{font-weight:900}

  /* Footer */
  .footer{position:absolute;left:0;top:1090px;width:907px;height:110px;background:var(--blue-band);
    display:flex;align-items:center;justify-content:center;text-align:center;
    font-weight:900;font-size:15.5px;line-height:1.4;color:var(--navy);padding:0 60px}
</style>
</head>
<body>
<main class="flyer">
  <div class="hero-photo" role="img" aria-label="Couple in sunglasses driving a red convertible sports car down an open road beneath dramatic sunlit clouds"></div>
  <h1 class="title"><span class="line-1">LANTERN OVER</span><span class="line-2">AMBER</span><span class="line-3">HILLS</span></h1>
  <div class="stripe"></div>

  <aside class="info-panel"></aside>
  <div class="badge">
    <span class="big">100's of people</span>
    <span class="mid dark">are joining every day</span>
    <span class="mid">and taking advantage</span>
    <span class="mid">of this once-in-a</span>
    <span class="small">lifetimeopportunity</span>
    <span class="cta">DON'T MISS OUT!</span>
  </div>

  <div class="hours">
    <div class="label-blue">Call Center Hours</div>
    <div class="day">Monday thru Friday</div>
    <div class="time">12PM to 9PM EST</div>
    <div class="day">Saturday:</div>
    <div class="time">12PM to 5PM EST</div>
  </div>
  <div class="phone phone-main">PHONE: (555) 314-2086</div>
  <div class="note note-pin">You will need the Call Center<br>Pin number when calling!</div>
  <div class="pin">Call Center Pin<br>Number: K4730</div>
  <div class="info-line">24-Hour Information Line</div>
  <div class="phone phone-info">(555) 870-1123</div>
  <div class="note note-listen">(Listen before contacting<br>&nbsp;the Call Center)</div>
  <div class="web-label">Website</div>
  <div class="web-url">www.threequicksteps-demo.com</div>

  <section class="intro">
    <h2>WHAT'S THE #1 SUCCESS FACTOR <span class="dark">IN EVERY HOME-BASED BUSINESS?</span></h2>
    <p>The answer is <strong>DUPLICATION!</strong> The key to building a highly successful home-based business is having a <strong>SYSTEM</strong> in place that everyone can easily follow… <strong>WE HAVE THAT SYSTEM IN PLACE!</strong></p>
    <p>It's a simple 3 steps proven postcard system that you can plug in immediately. The Entire Process Is Automated.</p>
  </section>

  <div class="section-bar bar-how">HERE'S HOW IT WORKS!</div>
  <ol class="steps">
    <li><span class="num">Step 1</span><span class="rule"></span><span>Your prospects receive your postcard in the mail</span></li>
    <li><span class="num">Step 2</span><span class="rule"></span><span>They listen to the 24-Hour Information Line and</span></li>
    <li><span class="num">Step 3</span><span class="rule"></span><span>They contact the Call Center to get their questions<br>answer and then close the sales for you</span></li>
  </ol>

  <div class="section-bar bar-speak">YOU NEVER HAVE TO SPEAK<br>TO ANYONE!</div>
  <ul class="benefits">
    <li><svg width="15" height="14" viewBox="0 0 15 14"><rect x="0.5" y="2.5" width="10" height="10" fill="none" stroke="#c0181d"/><path d="M2.5 7l3 3 8-9" fill="none" stroke="#c0181d" stroke-width="2.2"/></svg>50% fast start bonuses <strong>PAID WEEKLY!</strong></li>
    <li><svg width="15" height="14" viewBox="0 0 15 14"><rect x="0.5" y="2.5" width="10" height="10" fill="none" stroke="#c0181d"/><path d="M2.5 7l3 3 8-9" fill="none" stroke="#c0181d" stroke-width="2.2"/></svg>Receive a 100% Matching Bonus on all your personal sponsor member's income <strong>PAID WEEKLY!</strong></li>
    <li><svg width="15" height="14" viewBox="0 0 15 14"><rect x="0.5" y="2.5" width="10" height="10" fill="none" stroke="#c0181d"/><path d="M2.5 7l3 3 8-9" fill="none" stroke="#c0181d" stroke-width="2.2"/></svg>One-of-a-kind <strong>TWO TEAM</strong> compensation plan!</li>
    <li><svg width="15" height="14" viewBox="0 0 15 14"><rect x="0.5" y="2.5" width="10" height="10" fill="none" stroke="#c0181d"/><path d="M2.5 7l3 3 8-9" fill="none" stroke="#c0181d" stroke-width="2.2"/></svg>Receive the choice of <strong>50 FREE POST CARDS</strong> and <strong>50 FREE LEADS</strong> or <strong>20</strong> home business surveyed leads with first month product purchase!</li>
    <li><svg width="15" height="14" viewBox="0 0 15 14"><rect x="0.5" y="2.5" width="10" height="10" fill="none" stroke="#c0181d"/><path d="M2.5 7l3 3 8-9" fill="none" stroke="#c0181d" stroke-width="2.2"/></svg>Receive <strong>THREE</strong> professional websites for your business for FREE!</li>
    <li><svg width="15" height="14" viewBox="0 0 15 14"><rect x="0.5" y="2.5" width="10" height="10" fill="none" stroke="#c0181d"/><path d="M2.5 7l3 3 8-9" fill="none" stroke="#c0181d" stroke-width="2.2"/></svg>Global business already shipping to over 45 countries worldwide and expanding</li>
    <li><svg width="15" height="14" viewBox="0 0 15 14"><rect x="0.5" y="2.5" width="10" height="10" fill="none" stroke="#c0181d"/><path d="M2.5 7l3 3 8-9" fill="none" stroke="#c0181d" stroke-width="2.2"/></svg>30-Day - No Questions Asked, 100% Money Back Guarantee!</li>
  </ul>

  <footer class="footer">Due to the high volume of callers, if lines are busy, please keep trying to call into the Call Center or you can just go to the website and get enrolled right away to secure a top position.</footer>
</main>
</body>
</html>
```